professional business card design

Business card design. Photos have been uploaded and i am open to the designer choosing which photos to use. Would like the card to be mostyly in a grey scale design with black, whites, silver & grey colours. I have added copy of our flyer as would like on the back side of card our services to be listed. Do not use any bright colurs such as blue red green or yellow. i need to be able to edit the phone number and naem in the final card design submitted.

Target Market(s)

Clients

Industry/Entity Type

earhmovibng and transport

Contact Information for Business Card

Director Name, address, email, phone number and services

Colors

Designer to choose only greyscale colors for use in the design.

Requirements
Should not have
• no yellow, red, blue or green

```html
<!DOCTYPE html>
<html lang="en">
<head>
<meta charset="utf-8">
<title>KHS Pty Ltd – Business Card</title>
<link rel="stylesheet" href="https://fonts.googleapis.com/css2?family=Oswald:wght@500;600&family=Raleway:wght@400;500;600&display=swap">
<style>
  :root {
    --bg: #8a8a8a;
    --ink: #111111;
    --black: #0c0c0c;
    --charcoal: #1f1f1f;
    --steel: #9a9a9a;
    --silver: #c9c9c9;
    --paper: #f4f4f4;
    --white: #ffffff;
  }
  * { box-sizing: border-box; margin: 0; padding: 0; }
  html, body { width: 1200px; height: 1200px; overflow: hidden; }
  body {
    background: var(--bg);
    display: flex;
    flex-direction: column;
    align-items: center;
    justify-content: center;
    gap: 48px;
    font-family: "Raleway", sans-serif;
  }
  .card {
    position: relative;
    width: 900px;
    height: 514px;
    border-radius: 30px;
    overflow: hidden;
    box-shadow: 0 10px 28px rgba(0,0,0,.35);
  }

  /* Back: services + contact */
  .card-back { background: var(--black); }
  .services-panel {
    position: absolute; inset: 0 0 auto 0; height: 272px;
    background: linear-gradient(180deg, var(--white) 0%, #ececec 100%);
  }
  .services-panel::after {
    content: ""; position: absolute; left: 0; right: 0; bottom: -12px; height: 12px;
    background: var(--silver);
  }
  .services-title {
    position: absolute; top: 26px; left: 0; width: 56%;
    text-align: center;
    font-family: "Oswald", sans-serif; font-weight: 600;
    font-size: 38px; letter-spacing: .5px; color: var(--ink);
  }
  .services-list {
    position: absolute; list-style: none;
    font-family: "Oswald", sans-serif; font-weight: 500;
    font-size: 25px; line-height: 1.08; color: var(--ink); text-transform: uppercase;
  }
  .services-list li::before { content: "• "; }
  .services-list .cont { padding-left: 14px; }
  .services-list .cont::before { content: ""; }
  .list-left { top: 86px; left: 60px; }
  .list-right { top: 30px; left: 500px; }

  .contact-band {
    position: absolute; left: 0; right: 0; bottom: 0; height: 230px;
    background: linear-gradient(180deg, #2a2a2a 0%, var(--black) 70%);
    color: var(--white);
  }
  .person {
    position: absolute; top: 34px; left: 60px;
    border-left: 4px solid var(--white); padding-left: 14px;
  }
  .person-name { font-size: 40px; font-weight: 500; line-height: 1; letter-spacing: 1px; }
  .person-role { font-size: 22px; font-weight: 400; margin-top: 4px; color: var(--silver); }
  .contact-lines {
    position: absolute; list-style: none; font-size: 20px; line-height: 1.6;
  }
  .contact-lines li { display: flex; align-items: center; gap: 10px; }
  .contact-lines svg { width: 20px; height: 20px; flex: none; fill: var(--white); }
  .contact-left { left: 60px; top: 136px; }
  .contact-right { left: 440px; top: 34px; }
  .contact-right .indent { padding-left: 30px; margin-top: -6px; }

  /* Front: brand + fleet */
  .card-front {
    background: radial-gradient(ellipse at 45% 30%, #3a3a3a 0%, #1b1b1b 55%, var(--black) 100%);
  }
  .brand {
    position: absolute; top: 70px; left: 0; right: 0;
    display: flex; align-items: baseline; justify-content: center; gap: 18px;
    font-family: "Raleway", sans-serif; font-weight: 600; color: var(--silver);
  }
  .brand-name { font-size: 120px; letter-spacing: 6px; line-height: 1; }
  .brand-suffix { font-size: 40px; }
  .fleet-photo {
    position: absolute; left: 120px; right: 0; bottom: 0; height: 280px;
    background: linear-gradient(180deg, rgba(180,180,180,0) 0%, #7a7a7a 35%, #bdbdbd 60%, #4a4a4a 100%);
    border-top-left-radius: 60px;
  }
</style>
</head>
<body>

  <section class="card card-back" aria-label="Business card back">
    <div class="services-panel">
      <h2 class="services-title">OUR SERVICES</h2>
      <ul class="services-list list-left">
        <li>Over size loads / hot shot loads</li>
        <li>Heavy vehicle recovery services</li>
        <li>Potable water deliveries</li>
        <li>Road building / maintenance</li>
        <li>Earthworks</li>
        <li>Sand &amp; metal supply &amp; cartage</li>
      </ul>
      <ul class="services-list list-right">
        <li>Road train tippers</li>
        <li>Road train tankers</li>
        <li>Road train flat tops</li>
        <li>Drop deck trailers</li>
        <li>Mine site accredited</li>
        <li class="cont">Equipment &amp; operators</li>
      </ul>
    </div>

    <div class="contact-band">
      <div class="person">
        <p class="person-name">JOHN DOE</p>
        <p class="person-role">CEO | FOUNDER</p>
      </div>
      <ul class="contact-lines contact-left">
        <li><svg viewBox="0 0 24 24"><path d="M6.6 10.8a15 15 0 0 0 6.6 6.6l2.2-2.2c.3-.3.7-.4 1-.2 1.1.4 2.3.6 3.6.6.6 0 1 .4 1 1V20c0 .6-.4 1-1 1A17 17 0 0 1 3 4c0-.6.4-1 1-1h3.5c.6 0 1 .4 1 1 0 1.3.2 2.5.6 3.6.1.3 0 .7-.2 1z"/></svg>(000) 000 0000</li>
        <li><svg viewBox="0 0 24 24"><path d="M2 5h20v14H2zm2 2v.5l8 5 8-5V7zm0 3v7h16v-7l-8 5z"/></svg>email@youremail.com</li>
      </ul>
      <ul class="contact-lines contact-right">
        <li><svg viewBox="0 0 24 24"><path d="M12 2a10 10 0 1 0 0 20 10 10 0 0 0 0-20zm6.9 6h-3a15 15 0 0 0-1.3-4 8 8 0 0 1 4.3 4zM12 4c.8 1.2 1.5 2.5 1.9 4h-3.8c.4-1.5 1.1-2.8 1.9-4zM4.3 14a8 8 0 0 1 0-4h3.4a16 16 0 0 0 0 4zm.8 2h3a15 15 0 0 0 1.3 4 8 8 0 0 1-4.3-4zm3-8h-3a8 8 0 0 1 4.3-4 15 15 0 0 0-1.3 4zM12 20c-.8-1.2-1.5-2.5-1.9-4h3.8c-.4 1.5-1.1 2.8-1.9 4zm2.3-6H9.7a14 14 0 0 1 0-4h4.6a14 14 0 0 1 0 4zm.3 6a15 15 0 0 0 1.3-4h3a8 8 0 0 1-4.3 4zm1.7-6a16 16 0 0 0 0-4h3.4a8 8 0 0 1 0 4z"/></svg>www.yourwebsite.com</li>
        <li><svg viewBox="0 0 24 24"><path d="M12 2a7 7 0 0 0-7 7c0 5 7 13 7 13s7-8 7-13a7 7 0 0 0-7-7zm0 9.5a2.5 2.5 0 1 1 0-5 2.5 2.5 0 0 1 0 5z"/></svg>KHS Pty Ltd</li>
        <li class="indent">Depot: Lot 114, Ironbark Road Marla Creek</li>
      </ul>
    </div>
  </section>

  <section class="card card-front" aria-label="Business card front">
    <div class="brand">
      <span class="brand-name">KHS</span>
      <span class="brand-suffix">Pty Ltd</span>
    </div>
    <div class="fleet-photo" role="img" aria-label="Greyscale photo of a fleet of road train trucks"></div>
  </section>

</body>
</html>
```